Pitch Deck Design for Startup (Quorvo.io)

Graphic Design for Pitch Deck [Pitch Deck content in links below]

Who are we ?

“Quorvo” always, never “QUORVO”

Quorvo is an platform to easily use & publish algorithms with minimal effort.

Algorithms include:
Artificial Intelligence
Deep Learning
Machine Learning

No matter what type of applications or software users have, they can implement any of our State-of-Art AI algorithms in their apps with 3 lines of code.

Quorvo is untangling the hard parts™

Using Quorvo is as easy as just 3 lines of code to be up and running in minutes.

The general idea is that there's a central place for any app to find great algorithms when they want to use AI algorithms/models and implement them with extreme ease and speed, and this place is Quorvo.io.

For the information this deck needs to contain, please refer to this google slide: http://lnkshrt.example/7Tq9Wz, all the information in there are necessary, we need you to transform this deck into a much better looking, clear, colorful, and also stylish & concise deck. If you can give it a bit of Sci-Fi style would be great as well (not a must have)!

You have total freedom to design however you want, just remember three principles:

It needs to establish the brand / image of the Quorvo platform to the description above.

Our audience is wide - so use the ‘explain it like I am 5 year-old’ principle.

DO NOT assume specialist knowledge in the audience - make the deck extremely simple, clear, intuitive and compelling!
If there’s something you’re not sure about in the deck, anything, please don’t hesitate to ask us to get it right!!!

In terms of styles, what we like is something fun & modern but doesn’t lose a sense of quality (seriousness).

We want a clear storyline, and the current sequence and the way we organise the info is what we think is good, but it might not be the best way to present in the deck… additional slide ideas can be submitted with in the process.

QUESTIONS? If you have any questions or better suggestions on ANYTHING related to the deck, feel free to let us know at a@quorvo.io, we normally respond promptly.

The design of our website uses more than one colors, and it has slight movement when people scrolling as well. Something goes along with its design would be a nice attribute (Note: not a must have, feel free to design your way, if you try to go along with those colors but the deck doesn’t look good, the design would have a very low chance of being selected). Please take a look for your inspirations: http://quorvo.io.

Again, any questions, and enquiries, feel free to reach out to us: a@quorvo.io

Target Market(s)

Angel Investors (Tech Startups), Developers, Software Companies

Industry/Entity Type

Startup

Font styles to use
Serif

Requirements
Must have
• GOOD DECKS EXAMPLES:
• For your reference, here are some deck designs we like:
• Zelko, NestLoop, Palbridge
• http://lnkshrt.example/4Hd2Kp. The reason is: they are simple, clean, right on target, they used very simple but very friendly & nice colors. On every slide, the audience can kinda get the idea at the very first glance.
Nice to have
• If you can use multiple colors (themed in our style) , that would be awesome!
Should not have
• BAD DECKS EXAMPLES:
• The ones we don’t like: http://lnkshrt.example/9Rb6Nm, http://lnkshrt.example/3Fx8Jv. The reason? These are very tedious, not intuitive, and the design is very old fashioned. The information design of the deck is not giving great intuitions at the first sight, the audience has to go through all the text to get the idea.

```html
<!DOCTYPE html>
<html lang="en">
<head>
<meta charset="utf-8">
<title>Quorvo Pitch Deck</title>
<link href="https://fonts.googleapis.com/css2?family=Open+Sans:wght@400;600;700&family=Roboto+Condensed:wght@400;500&display=swap" rel="stylesheet">
<style>
  :root{
    --page:#ffffff;
    --slide:#2d3e50;
    --slide-deep:#263546;
    --sky:#5bc8f5;
    --sky-soft:#9fdcf8;
    --lilac:#d7c1ef;
    --lilac-soft:#e8d9f7;
    --ink:#1d2b3a;
    --white:#ffffff;
    --chart-bg:#e2e3e5;
    --trend:#c8474b;
    --trend-faint:#e2b4b5;
    --frame:#3a4756;
    --chin:#c9cdd2;
  }
  *{box-sizing:border-box;margin:0;padding:0}
  html,body{width:1200px;height:1022px;overflow:hidden;background:var(--page)}
  body{position:relative;font-family:"Open Sans",Arial,sans-serif;color:var(--white)}
  .slide{position:absolute;width:561px;height:308px;background:var(--slide);overflow:hidden}
  .slide--cover{left:25px;top:25px}
  .slide--demand{left:615px;top:25px}
  .slide--problems{left:25px;top:357px}
  .slide--trends{left:615px;top:357px}
  .slide--access{left:25px;top:690px}
  .slide--search{left:615px;top:690px}
  .abs{position:absolute}
  .slide-title{position:absolute;font-size:25px;font-weight:400;color:var(--lilac);line-height:1}
  .heading{position:absolute;font-size:24px;font-weight:400;color:var(--sky);line-height:1;white-space:nowrap}
  .bullets{position:absolute;list-style:none;font-size:10px;line-height:13px;color:var(--white)}
  .bullets li{position:relative;padding-left:12px}
  .bullets li::before{content:"";position:absolute;left:2px;top:5px;width:4px;height:4px;background:var(--white);transform:rotate(45deg)}

  /* cover */
  .cover-pattern{left:0;top:0;width:74px;height:308px;background:linear-gradient(180deg,var(--sky) 0%,var(--lilac) 35%,var(--sky) 65%,var(--lilac) 100%);opacity:.85}
  .wordmark{left:175px;top:96px;display:flex;align-items:center;gap:14px}
  .wordmark-square{width:34px;height:34px;background:var(--lilac)}
  .wordmark-name{font-size:50px;font-weight:700;color:var(--white);line-height:1}
  .tagline{left:158px;top:203px;font-size:24px;color:var(--lilac);white-space:nowrap}

  /* chart */
  .chart{left:43px;top:57px;width:473px;height:224px;background:var(--chart-bg)}
  .chart-source{left:4px;bottom:2px;font-size:12px;color:#c9c3c6}

  .icon-placeholder{position:absolute;border-radius:6px;background:linear-gradient(135deg,var(--lilac),var(--sky));opacity:.75}

  /* devices */
  .device{position:absolute;border-radius:12px;background:var(--frame);overflow:hidden}
  .device-screen{position:absolute;left:16px;top:15px;right:16px;bottom:50px}
  .device-chin{position:absolute;left:0;right:0;bottom:0;height:32px;background:linear-gradient(180deg,#e7e9ec,var(--chin))}
  .callout{position:absolute;background:var(--sky);color:var(--ink);font-family:"Roboto Condensed",Arial,sans-serif;font-weight:400;text-align:center;line-height:1.2}
</style>
</head>
<body>

<section class="slide slide--cover">
  <div class="abs cover-pattern" role="img" aria-label="Column of overlapping blue and lilac diamond tiles"></div>
  <div class="abs wordmark"><span class="wordmark-square"></span><span class="wordmark-name">Quorvo</span></div>
  <p class="abs tagline">AI Anywhere, Anytime</p>
</section>

<section class="slide slide--demand">
  <h2 class="slide-title" style="left:13px;top:13px">Everyone Wants AI</h2>
  <div class="abs chart">
    <svg width="473" height="224" viewBox="0 0 473 224">
      <polyline fill="none" stroke="var(--trend-faint)" stroke-width="1.6" points="0,145 10,160 20,150 30,165 40,150 50,160 60,150 70,158 85,148 100,160 115,150 130,165 145,150 160,158 175,150 190,162 205,150 220,158 235,145 250,150 262,132 275,140 290,125 305,135 320,115 335,125 350,105 362,118 375,92 390,100 405,70 420,78 435,40 447,20 458,30 465,70 473,10"/>
      <polyline fill="none" stroke="var(--trend-faint)" stroke-width="1.6" points="0,222 40,222 80,215 120,214 160,210 200,205 240,200 260,196 280,190 300,178 320,172 340,160 360,150 380,130 400,105 420,80 440,50 455,30 465,60 473,25"/>
      <polyline fill="none" stroke="var(--trend)" stroke-width="2" points="0,205 10,198 22,210 35,200 50,212 65,204 80,214 95,205 110,209 125,215 140,213 155,220 170,215 185,218 200,215 215,212 235,215 250,225 265,218 280,222 295,210 310,216 320,204 335,197 350,203 362,195 375,197 388,183 400,178 410,172 422,166 430,148 440,180 450,168 458,160 465,145 473,120" transform="translate(0,-42)"/>
    </svg>
    <span class="abs chart-source">Source: SearchPulse</span>
  </div>
</section>

<section class="slide slide--problems">
  <h2 class="slide-title" style="left:21px;top:14px">But</h2>

  <h3 class="heading" style="left:24px;top:54px">Rare Talents</h3>
  <ul class="bullets" style="left:24px;top:86px;width:170px">
    <li>Well trained AI talents are really hard to find.</li>
  </ul>
  <div class="icon-placeholder" style="left:142px;top:118px;width:96px;height:44px" role="img" aria-label="Group icon with a magnifying glass over one figure"></div>

  <h3 class="heading" style="left:299px;top:54px">Steep Learning Curve</h3>
  <ul class="bullets" style="left:299px;top:86px;width:190px">
    <li>AI takes a long time to learn, it's hard for normal developers to develop AI.</li>
    <li>Even slightly customising &amp; modifying AI algorithms can be challenging.</li>
  </ul>
  <svg class="abs" style="left:492px;top:128px" width="46" height="42" viewBox="0 0 46 42" fill="none" stroke="var(--sky)" stroke-width="2.4" stroke-linecap="round" stroke-linejoin="round">
    <polyline points="3,2 3,39 44,39"/>
    <path d="M8 35 C16 22, 26 12, 40 5"/>
    <polyline points="33,4 41,4 39,12"/>
  </svg>

  <h3 class="heading" style="left:24px;top:176px">Long Dev Process</h3>
  <ul class="bullets" style="left:24px;top:209px;width:168px">
    <li>Finding the right Ai solution &amp; AI development are time consuming.</li>
    <li>Infrastructures need to be very well configured for the best performance.</li>
  </ul>
  <svg class="abs" style="left:200px;top:238px" width="48" height="48" viewBox="0 0 48 48" fill="none" stroke="var(--sky-soft)" stroke-width="2.6" stroke-linecap="round">
    <path d="M42 24 A19 19 0 1 1 33 8"/>
    <polyline points="24,12 24,25 32,31"/>
    <polyline points="37,26 42,31 46,25"/>
  </svg>

  <h3 class="heading" style="left:299px;top:176px">Repeated Works</h3>
  <ul class="bullets" style="left:299px;top:209px;width:180px">
    <li>Most people are re-training the same/very similar AI models and hosting them separately for use.</li>
  </ul>
  <div class="icon-placeholder" style="left:487px;top:238px;width:50px;height:50px" role="img" aria-label="Icon of a person working at a desk with refresh arrows"></div>
</section>

<section class="slide slide--trends">
  <h2 class="slide-title" style="left:14px;top:14px">Meanwhile</h2>

  <h3 class="heading" style="left:195px;top:46px;font-size:26px">AI Algorithmic Interests</h3>
  <svg class="abs" style="left:104px;top:82px" width="52" height="52" viewBox="0 0 52 52">
    <g stroke="var(--sky)" stroke-width="3">
      <line x1="15" y1="2" x2="15" y2="10"/><line x1="22" y1="2" x2="22" y2="10"/><line x1="30" y1="2" x2="30" y2="10"/><line x1="37" y1="2" x2="37" y2="10"/>
      <line x1="15" y1="42" x2="15" y2="50"/><line x1="22" y1="42" x2="22" y2="50"/><line x1="30" y1="42" x2="30" y2="50"/><line x1="37" y1="42" x2="37" y2="50"/>
      <line x1="2" y1="15" x2="10" y2="15"/><line x1="2" y1="22" x2="10" y2="22"/><line x1="2" y1="30" x2="10" y2="30"/><line x1="2" y1="37" x2="10" y2="37"/>
      <line x1="42" y1="15" x2="50" y2="15"/><line x1="42" y1="22" x2="50" y2="22"/><line x1="42" y1="30" x2="50" y2="30"/><line x1="42" y1="37" x2="50" y2="37"/>
    </g>
    <rect x="9" y="9" width="34" height="34" rx="3" fill="var(--sky)"/>
    <text x="26" y="31" text-anchor="middle" font-family="Open Sans, sans-serif" font-weight="700" font-size="14" fill="var(--white)">AI</text>
  </svg>
  <ul class="bullets" style="left:195px;top:92px;width:340px">
    <li>AI has been proven to deliver great results.</li>
    <li>Digital products are (looking for) implementing AI in software.</li>
    <li>AI has already became the “Next Big Thing”</li>
  </ul>

  <h3 class="heading" style="left:195px;top:150px;font-size:26px">API Boom</h3>
  <svg class="abs" style="left:97px;top:189px" width="67" height="60" viewBox="0 0 67 60">
    <rect x="0" y="0" width="67" height="46" rx="3" fill="var(--sky)"/>
    <rect x="4" y="4" width="59" height="36" fill="var(--white)"/>
    <rect x="28" y="46" width="11" height="8" fill="var(--sky)"/>
    <rect x="22" y="54" width="23" height="4" fill="var(--sky)"/>
  </svg>
  <ul class="bullets" style="left:195px;top:199px;width:320px">
    <li>Most sophisticated digital products are heavily relying on APIs to interconnect components &amp; integrate w/ services.</li>
    <li>APIs are turning the world into a giant computer.</li>
  </ul>

  <h3 class="heading" style="left:195px;top:254px;font-size:26px">Are Biggest Tech Trends</h3>
</section>

<section class="slide slide--access">
  <div class="device" style="left:97px;top:21px;width:387px;height:264px">
    <div class="device-screen" role="img" aria-label="Marketplace website home page with a teal diamond hero and a sign up button" style="background:linear-gradient(135deg,#00e8c8 0%,#00e8c8 45%,#f7f8fa 46%,#ffffff 100%)"></div>
    <div class="device-chin"></div>
  </div>
  <svg class="abs" style="left:405px;top:196px" width="30" height="32" viewBox="0 0 30 32"><polygon points="26,0 30,32 0,32" fill="var(--sky)"/></svg>
  <div class="callout" style="left:135px;top:224px;width:313px;height:53px;padding-top:5px;font-size:19px">So We Give Everyone Instant Access<br>to State-of-Art AI Algorithms.</div>
</section>

<section class="slide slide--search">
  <div class="device" style="left:86px;top:21px;width:386px;height:264px">
    <div class="device-screen" role="img" aria-label="Algorithm documentation page with a search results list" style="background:linear-gradient(90deg,#7d8287 0%,#7d8287 50%,#f2f3f4 50%,#ffffff 100%)"></div>
    <div class="device-chin"></div>
  </div>
  <div class="callout" style="left:89px;top:89px;width:190px;height:40px;padding-top:8px;font-size:19px">Just Search For It</div>
</section>

</body>
</html>
```